Design some Business Cards for Birch Meadow

could someone please design some snazzy business cards for "Birch Meadow"
the website is birchmeadow.co.nz

the logo is attached

name : Harriet Doucan
Contact Number: 0224819357
email: harrietdouc@birchmeadow.co.nz
Slogan: Competitive prices, and personal service in the Wanganui district

The theme is green as its for a lawn mowing outfit!

```html
<!DOCTYPE html>
<html lang="en">
<head>
<meta charset="utf-8">
<title>Birch Meadow – Business Cards</title>
<link rel="stylesheet" href="https://fonts.googleapis.com/css2?family=Gelasio:wght@400;700&family=Open+Sans:wght@400;600&display=swap">
<style>
  :root {
    --green: #5a7300;
    --green-mid: #4c6200;
    --green-dark: #3e5100;
    --white: #ffffff;
    --backdrop: #e4e4e4;
    --shadow: rgba(0, 0, 0, 0.18);
  }
  * { box-sizing: border-box; margin: 0; padding: 0; }
  html, body {
    width: 1200px; height: 753px; overflow: hidden;
    background: var(--backdrop);
  }
  .canvas {
    position: relative; width: 1200px; height: 753px;
    font-family: "Open Sans", Arial, sans-serif;
  }
  .card {
    position: absolute; top: 216px; width: 553px; height: 320px;
    box-shadow: 0 4px 14px var(--shadow);
    overflow: hidden;
  }
  .card--front { left: 40px; display: flex; }
  .card--back { left: 607px; background: var(--green);
    display: flex; align-items: center; justify-content: center; }

  .front__brand {
    width: 265px; height: 100%; background: var(--white);
    display: flex; flex-direction: column; align-items: center; justify-content: center;
  }
  .front__stripes { display: flex; height: 100%; }
  .front__stripes span { display: block; width: 10px; height: 100%; }
  .front__stripes .stripe-dark { background: var(--green-dark); }
  .front__stripes .stripe-mid { background: var(--green-mid); }

  .front__details {
    flex: 1; background: var(--green); color: var(--white);
    padding: 26px 18px 0 22px;
  }
  .holder-name {
    font-family: "Gelasio", Georgia, serif; font-weight: 400;
    font-size: 25px; text-align: center; margin-bottom: 34px;
  }
  .contact-list { list-style: none; }
  .contact-list li {
    display: flex; align-items: center; gap: 8px;
    font-size: 12.5px; margin-bottom: 9px; white-space: nowrap;
  }
  .contact-icon { width: 24px; height: 24px; flex: none; }
  .slogan {
    position: relative; margin-top: 46px;
    font-size: 12.5px; line-height: 1.4; text-align: center; padding: 0 14px;
  }
  .slogan .quote-mark {
    position: absolute; font-family: "Gelasio", Georgia, serif;
    font-size: 26px; font-weight: 700; line-height: 1;
  }
  .slogan .quote-open { left: 0; top: -4px; }
  .slogan .quote-close { right: 2px; bottom: -14px; }

  .brand-mark {
    display: flex; flex-direction: column; align-items: center; gap: 14px;
  }
  .brand-dot { width: 22px; height: 22px; border-radius: 50%; }
  .brand-name {
    font-family: "Gelasio", Georgia, serif; font-weight: 700; font-size: 17px;
  }
  .brand-mark--light .brand-dot { background: var(--green); }
  .brand-mark--light .brand-name { color: var(--green); }
  .brand-mark--dark .brand-dot { background: var(--white); }
  .brand-mark--dark .brand-name { color: var(--white); }
</style>
</head>
<body>
<main class="canvas">
  <section class="card card--front" aria-label="Business card front">
    <div class="front__brand">
      <div class="brand-mark brand-mark--light">
        <span class="brand-dot"></span>
        <span class="brand-name">Birch Meadow</span>
      </div>
    </div>
    <div class="front__stripes">
      <span class="stripe-dark"></span><span class="stripe-mid"></span>
    </div>
    <div class="front__details">
      <h1 class="holder-name">Harriet Doucan</h1>
      <ul class="contact-list">
        <li>
          <svg class="contact-icon" viewBox="0 0 24 24" aria-hidden="true">
            <circle cx="12" cy="12" r="12" fill="#fff"/>
            <path d="M8.3 6.5l1.8-.4 1.3 2.8-1.2 1c.6 1.4 1.6 2.4 3 3l1-1.2 2.8 1.3-.4 1.8c-4.6.4-8.7-3.7-8.3-8.3z" fill="#5a7300"/>
          </svg>
          <span>0224819357</span>
        </li>
        <li>
          <svg class="contact-icon" viewBox="0 0 24 24" aria-hidden="true">
            <circle cx="12" cy="12" r="12" fill="#fff"/>
            <rect x="6" y="8" width="12" height="8.5" fill="#5a7300"/>
            <path d="M6.3 8.3l5.7 4.6 5.7-4.6" fill="none" stroke="#fff" stroke-width="1.2"/>
          </svg>
          <span>harrietdouc@birchmeadow.co.nz</span>
        </li>
        <li>
          <svg class="contact-icon" viewBox="0 0 24 24" aria-hidden="true">
            <circle cx="12" cy="12" r="12" fill="#fff"/>
            <path d="M13 6.5l5 4.5-5 4.5v-2.6c-3 0-5 .9-6.5 3.1.5-3.6 2.6-6.1 6.5-6.6z" fill="#5a7300"/>
          </svg>
          <span>www.birchmeadow.co.nz</span>
        </li>
      </ul>
      <p class="slogan">
        <span class="quote-mark quote-open">&ldquo;</span>Competitive prices, and personal service in the Wanganui district<span class="quote-mark quote-close">&rdquo;</span>
      </p>
    </div>
  </section>

  <section class="card card--back" aria-label="Business card back">
    <div class="brand-mark brand-mark--dark">
      <span class="brand-dot"></span>
      <span class="brand-name">Birch Meadow</span>
    </div>
  </section>
</main>
</body>
</html>
```